Brackwell Removals

We are a domestic removals company, providing the following service:
- removals service
- packing service
- packing materials
- storage facility
- furniture dismantling and reassembling
We would like to start a flyer campaign to customers that just agreed for the house sale.
Our strong key points:
- Good Reviews (Revuemark, Zentrix, shiftquote.com and pagebook)
- Two Men Service (we do all the heavy work for the customer, and place the furniture and boxes to each room of destination)
- Fully Insured
- We can take bookings 7-days of week
- Free and no-obligation survey (we need to do a house visit first in order to provide a fixed and accurate quote)
- Free Quote
Technical Specs:
Landline number: 01632 960418
Contact email: office@brackwellremovals.example.co.uk
Address: Unit 14, Carrow Lane, Northampton NN9 4QT
Website: brackwellremovals.example.co.uk
Took a look on the onto previous projects on FX.com, and liked several flyers already done by you guys, for this industry
We'd like to integrate the colours from our logo in the flyer as well !!

```html
<!DOCTYPE html>
<html lang="en">
<head>
<meta charset="utf-8">
<title>Brackwell Removals – Flyer</title>
<link rel="stylesheet" href="https://fonts.googleapis.com/css2?family=Russo+One&family=Open+Sans:wght@400;600;700&family=Lato:wght@400;700;900&display=swap">
<style>
  :root {
    --bg: #e8e4de;
    --paper: #ffffff;
    --ink: #1d1e22;
    --slate: #3e5a72;
    --rust: #b4511f;
    --rust-dark: #8f3e16;
    --white: #ffffff;
    --sepia-a: #c9a489;
    --sepia-b: #7a5540;
    --steel-a: #5d7590;
    --steel-b: #2b3a4c;
  }
  * { box-sizing: border-box; margin: 0; padding: 0; }
  html, body { width: 1200px; height: 800px; overflow: hidden; }
  body { background: var(--bg); font-family: "Open Sans", sans-serif; position: relative; }

  .flyer {
    position: absolute; left: 330px; top: 18px;
    width: 540px; height: 764px;
    background: var(--paper); overflow: hidden;
    box-shadow: 0 6px 22px rgba(0,0,0,.18);
  }

  .brand {
    position: absolute; left: 26px; top: 104px;
    display: flex; align-items: center; gap: 10px;
  }
  .brand-dot { width: 44px; height: 44px; border-radius: 50%; background: var(--slate); }
  .brand-name {
    font-family: "Russo One", sans-serif; font-size: 20px;
    color: var(--slate); text-transform: uppercase; line-height: 1.05;
  }

  .intro {
    position: absolute; left: 0; top: 96px; width: 540px; height: 324px;
    background: var(--ink);
    clip-path: polygon(0 26%, 100% 0, 100% 100%, 0 100%);
  }
  .headline {
    position: absolute; left: 28px; top: 204px;
    font-family: "Russo One", sans-serif; font-size: 23px; line-height: 1.14;
    color: var(--white); text-transform: uppercase;
  }
  .services {
    position: absolute; left: 34px; top: 306px;
    list-style: none; color: var(--white); font-size: 15.5px; line-height: 1.32;
  }
  .services li::before { content: "• "; }

  .photo { position: absolute; }
  .photo-circle { border-radius: 50%; border: 5px solid var(--rust); }
  .photo-van { left: 330px; top: 14px; width: 180px; height: 180px;
    background: radial-gradient(circle at 40% 45%, var(--sepia-a), var(--sepia-b)); }
  .photo-warehouse { left: 300px; top: 196px; width: 116px; height: 116px;
    background: linear-gradient(160deg, var(--steel-a), var(--steel-b)); }
  .photo-carrier { left: 424px; top: 206px; width: 100px; height: 100px;
    background: radial-gradient(circle at 50% 45%, #e6e6e6, #8c8f94); }

  .key-points {
    position: absolute; left: 0; top: 420px; width: 540px; height: 220px;
    background: var(--slate); padding: 12px 24px 0;
    color: var(--white);
  }
  .key-title {
    font-family: "Russo One", sans-serif; font-size: 26px; line-height: 1.2;
    text-transform: uppercase; margin-bottom: 6px;
  }
  .key-cols { display: flex; gap: 18px; }
  .key-cols ul { list-style: none; flex: 1; }
  .key-cols li { font-family: "Lato", sans-serif; font-weight: 900; font-size: 12.5px;
    text-transform: uppercase; line-height: 1.25; margin-bottom: 3px; }
  .key-cols li::before { content: "• "; }
  .key-cols small { display: block; font-weight: 400; font-size: 10px;
    text-transform: none; line-height: 1.25; }

  .footer {
    position: absolute; left: 0; top: 640px; width: 540px; height: 124px;
    background: var(--rust);
  }
  .photo-strip { position: absolute; left: 14px; top: 602px; display: flex; gap: 10px; }
  .photo-rect { height: 90px; border: 4px solid var(--rust-dark); }
  .photo-tape { width: 170px; background: linear-gradient(150deg, #3b4868, #1f2433); }
  .photo-crew { width: 166px; background: linear-gradient(150deg, #b89070, #2e3446); }
  .photo-boxes { width: 166px; background: linear-gradient(150deg, #a78566, #2a2522); }

  .contact {
    position: absolute; left: 0; top: 698px; width: 540px;
    text-align: center; color: var(--white); font-family: "Lato", sans-serif;
    font-size: 10.5px; line-height: 1.4;
  }
  .contact-title { font-weight: 900; font-size: 12px; text-transform: uppercase; }
</style>
</head>
<body>
  <article class="flyer">
    <div class="intro"></div>

    <div class="brand">
      <span class="brand-dot"></span>
      <span class="brand-name">Brackwell<br>Removals</span>
    </div>

    <div class="photo photo-circle photo-van" role="img" aria-label="Mover loading boxes into a van"></div>
    <div class="photo photo-circle photo-warehouse" role="img" aria-label="Storage warehouse with shelving"></div>
    <div class="photo photo-circle photo-carrier" role="img" aria-label="Mover carrying a box"></div>

    <h1 class="headline">Removals in<br>Northampton &amp;<br>Surroundings</h1>
    <ul class="services">
      <li>Removals Service</li>
      <li>Packing Service</li>
      <li>Packing Materials</li>
      <li>Storage Facility</li>
      <li>Furniture Dismantling And Reassembling</li>
    </ul>

    <section class="key-points">
      <h2 class="key-title">Our Strong Key Points:</h2>
      <div class="key-cols">
        <ul>
          <li>Good Reviews<small>(Revuemark, Zentrix, shiftquote.com and pagebook)</small></li>
          <li>Two Men Service<small>(we do all the heavy work for the customer, and place the furniture and boxes to each room of destination)</small></li>
          <li>Fully Insured</li>
        </ul>
        <ul>
          <li>We can take bookings 7-days of week</li>
          <li>Free and no-obligation survey<small>(we need to do a house visit first in order to provide a fixed and accurate quote)</small></li>
          <li>Free Quote</li>
        </ul>
      </div>
    </section>

    <footer class="footer"></footer>
    <div class="photo-strip">
      <div class="photo-rect photo-tape" role="img" aria-label="Mover taping a cardboard box"></div>
      <div class="photo-rect photo-crew" role="img" aria-label="Two movers unloading boxes from a van"></div>
      <div class="photo-rect photo-boxes" role="img" aria-label="Mover stacking boxes in a van"></div>
    </div>

    <div class="contact">
      <p class="contact-title">Contact Info:</p>
      <p>Ph: 01632 960418 | Email: office@brackwellremovals.example.co.uk</p>
      <p>Web: brackwellremovals.example.co.uk</p>
      <p>Add: Unit 14, Carrow Lane, Northampton NN9 4QT</p>
    </div>
  </article>
</body>
</html>
```